Veranaxis Business Card and Letter Head

We are a leadership assessment consultancy based in Sydney, Australia. We help executive-level decison-makers select leaders for more senior level roles in corporate and government organisations. Our methodology is based on the latest research from the field of neuroscience.
We need a business card design and matching letter head that presents our company, Veranaxis, as a:
1. trusted adviser to senior executive-level decison makers
2. niche consultancy who are experts in the field of assessing leadership talent
3. results-focused solution provider who balance scientific methods with pragmatic solutions
The following company details should be used in all designs:
Company Name: Veranaxis
Details (for business card):
Daniel Prescott
Senior Talent Advisor
Level 14, Brenning Tower
7 Brenning Square
Carrowby, NSW 2190 Australia
Phone: 1300 482 716
Mobile: 0412 573 208
Email: daniel.prescott@veranaxis.com.au
Website: veranaxis.com.au
I have attached the logo for Veranaxis (for both a white and black background) - your business card and letter head designs must incoporate this logo and colour scheme.
Thanks for your interest in this project, I'm looking forward to receiving your ideas.
Regards,
Daniel
Executive-level decison-makers in corporate and government organisations (e.g., CEO, VP, Head of Human Resources)
Leadership

```html
<!DOCTYPE html>
<html lang="en">
<head>
<meta charset="utf-8">
<title>Veranaxis Business Card</title>
<link href="https://fonts.googleapis.com/css2?family=Arimo:wght@400;700&display=swap" rel="stylesheet">
<style>
  :root {
    --page: #ffffff;
    --card-dark: #2a2929;
    --card-light: #ffffff;
    --ink: #2e2e2e;
    --ink-soft: #3c3c3c;
    --label: #b3b3b3;
    --name-light: #d9d9d9;
    --tagline: #9c9c9c;
    --accent: #c4281c;
  }
  * { box-sizing: border-box; margin: 0; padding: 0; }
  html, body {
    width: 1200px;
    height: 610px;
    overflow: hidden;
    background: var(--page);
    font-family: "Arimo", Arial, sans-serif;
  }
  .canvas {
    width: 1200px;
    height: 610px;
    display: flex;
    flex-direction: column;
    align-items: center;
    justify-content: center;
    gap: 14px;
  }
  .card {
    width: 460px;
    height: 280px;
    position: relative;
    box-shadow: 0 3px 8px rgba(0, 0, 0, 0.22);
  }
  .card--front {
    background: var(--card-dark);
    display: flex;
    flex-direction: column;
    justify-content: center;
    align-items: center;
  }
  .brand {
    display: flex;
    align-items: center;
    gap: 18px;
  }
  .brand__square {
    width: 44px;
    height: 44px;
    background: var(--accent);
  }
  .brand__name {
    font-weight: 700;
    font-size: 56px;
    letter-spacing: -1.5px;
    color: var(--name-light);
    line-height: 1;
  }
  .tagline {
    margin-top: 12px;
    margin-left: 62px;
    font-size: 14px;
    letter-spacing: 0.6px;
    color: var(--tagline);
  }
  .card--back {
    background: var(--card-light);
    padding: 18px 22px;
  }
  .mini-brand {
    display: flex;
    align-items: center;
    gap: 8px;
  }
  .mini-brand__square {
    width: 18px;
    height: 18px;
    background: var(--accent);
  }
  .mini-brand__name {
    font-weight: 700;
    font-size: 18px;
    color: var(--ink);
  }
  .details {
    margin-left: 104px;
    margin-top: 16px;
    color: var(--ink-soft);
    font-size: 16px;
    line-height: 1.22;
  }
  .details__name { font-weight: 700; color: var(--ink); }
  .details__address { margin-top: 12px; }
  .contact {
    margin-top: 12px;
    display: grid;
    grid-template-columns: 28px auto;
    line-height: 1.22;
  }
  .contact__label {
    font-weight: 700;
    color: var(--label);
    text-align: right;
    padding-right: 6px;
  }
  .contact__web { font-weight: 700; color: var(--ink); }
</style>
</head>
<body>
  <main class="canvas">
    <section class="card card--front">
      <div class="brand">
        <span class="brand__square"></span>
        <span class="brand__name">Veranaxis</span>
      </div>
      <p class="tagline">ASSESSING EXECUTIVE CALIBRE</p>
    </section>

    <section class="card card--back">
      <div class="mini-brand">
        <span class="mini-brand__square"></span>
        <span class="mini-brand__name">Veranaxis</span>
      </div>
      <div class="details">
        <p class="details__name">Daniel Prescott</p>
        <p class="details__title">Senior Talent Advisor</p>
        <p class="details__address">Level 14, Brenning Tower<br>7 Brenning Square<br>Carrowby, NSW 2190 Australia</p>
        <div class="contact">
          <span class="contact__label">p:</span><span>1300 482 716</span>
          <span class="contact__label">m:</span><span>0412 573 208</span>
          <span class="contact__label">e:</span><span>daniel.prescott@veranaxis.com.au</span>
          <span class="contact__label">w:</span><span class="contact__web">veranaxis.com.au</span>
        </div>
      </div>
    </section>
  </main>
</body>
</html>
```